Business card Pfotenweide

Business card is for a self-employed dog trainer with own dog school. Name and logo of the dog school are available. Color specifications as well. The design should be classy and minimalist, but also modern. An already existing idea would be: Front: Only the logo Back: Contact data

Font styles to use
Serif
Sans Serif
Other font styles liked:
• Trajan Pro

Colors
f78f20

Requirements
Must have
• Name: Marlene Kessel-Brand Title: Dipl. Dog Trainer Contain my logo Follow my font and color preferences (see files)

```html
<!DOCTYPE html>
<html lang="de">
<head>
<meta charset="utf-8">
<title>Pfotenweide – Business Card</title>
<link rel="stylesheet" href="https://fonts.googleapis.com/css2?family=Cinzel:wght@400&family=Work+Sans:wght@300;400;700&display=swap">
<style>
  :root {
    --stage: #e7e2da;
    --card: #232323;
    --card-shade: #2c2c2c;
    --orange: #f78f20;
    --white: #ffffff;
    --text-light: #ececec;
  }
  * { box-sizing: border-box; margin: 0; padding: 0; }
  html, body { width: 1200px; height: 930px; overflow: hidden; }
  body {
    background: var(--stage);
    position: relative;
    font-family: "Work Sans", Arial, sans-serif;
  }
  .card {
    position: absolute;
    left: 278px;
    width: 644px;
    height: 369px;
    background: var(--card);
    border-radius: 24px;
    overflow: hidden;
    box-shadow: 0 6px 18px rgba(0,0,0,0.25);
  }
  .card--front { top: 75px; }
  .card--back { top: 486px; }

  .card__decoration {
    position: absolute;
    background: radial-gradient(ellipse at center, var(--card-shade) 0%, rgba(44,44,44,0.6) 55%, rgba(35,35,35,0) 75%);
  }
  .card--front .card__decoration { left: 150px; top: 0; width: 480px; height: 369px; }
  .card--back .card__decoration { left: 50px; top: 0; width: 560px; height: 369px; }

  .card__band {
    position: absolute;
    left: 0; top: 0;
    width: 58px; height: 100%;
    background: var(--orange);
  }
  .brand-mark {
    position: absolute;
    border-radius: 50%;
    background: var(--white);
  }
  .card--front .brand-mark {
    left: 12px; top: 31px;
    width: 92px; height: 92px;
    border: 4px solid var(--card);
    box-shadow: 0 0 0 2px var(--white) inset;
  }
  .brand {
    position: absolute;
    font-family: "Cinzel", "Trajan Pro", Georgia, serif;
    color: var(--white);
    line-height: 1;
  }
  .brand__name { display: block; font-weight: 400; }
  .brand__url {
    display: block;
    font-family: "Cinzel", Georgia, serif;
    color: var(--orange);
  }
  .card--front .brand { left: 124px; top: 64px; }
  .card--front .brand__name { font-size: 25px; letter-spacing: 0.5px; }
  .card--front .brand__url { font-size: 6px; letter-spacing: 5.4px; margin-top: 1px; }

  .person {
    position: absolute;
    right: 35px; top: 190px;
    text-align: right;
  }
  .person__name {
    font-weight: 700;
    font-size: 22px;
    color: var(--orange);
    letter-spacing: 0.2px;
  }
  .person__title {
    font-weight: 300;
    font-size: 16px;
    color: var(--text-light);
    margin-top: 2px;
  }
  .divider {
    position: absolute;
    left: 124px; right: 35px; top: 258px;
    height: 1px;
    background: var(--orange);
    opacity: 0.85;
  }
  .address {
    position: absolute;
    left: 124px; top: 296px;
    font-style: normal;
    font-weight: 300;
    font-size: 16px;
    line-height: 20px;
    color: var(--text-light);
  }
  .contacts {
    position: absolute;
    right: 35px; top: 276px;
    list-style: none;
    font-weight: 300;
    font-size: 16px;
    line-height: 20.5px;
    color: var(--text-light);
    text-align: right;
  }
  .contacts li { display: flex; align-items: center; justify-content: flex-end; gap: 10px; }
  .contacts svg { width: 11px; height: 11px; flex: none; }

  .card--back .brand-mark {
    left: 242px; top: 79px;
    width: 160px; height: 160px;
    border: 6px solid var(--card);
    box-shadow: 0 0 0 2px var(--white) inset;
  }
  .card--back .brand {
    left: 0; right: 0; top: 248px;
    text-align: center;
  }
  .card--back .brand__name { font-size: 42px; letter-spacing: 1px; }
  .card--back .brand__url { font-size: 9px; letter-spacing: 9px; margin-top: 3px; padding-left: 9px; }
</style>
</head>
<body>
  <section class="card card--front" aria-label="Business card front">
    <div class="card__decoration" role="img" aria-label="Large faint silhouette of a dog and a small dog in the background"></div>
    <div class="card__band"></div>
    <div class="brand-mark"></div>
    <div class="brand">
      <span class="brand__name">PFOTENWEIDE</span>
      <span class="brand__url">www.pfotenweide.ch</span>
    </div>
    <div class="person">
      <p class="person__name">MARLENE KESSEL-BRAND</p>
      <p class="person__title">Dipl. Dog Trainer</p>
    </div>
    <div class="divider"></div>
    <address class="address">Lindenweg 12,<br>Uster</address>
    <ul class="contacts">
      <li>(044) 555-0142
        <svg viewBox="0 0 12 12" aria-hidden="true"><path d="M3 1.2 4.6 3.4 3.6 4.6c.6 1.5 1.9 2.9 3.6 3.7l1.1-1 2.2 1.6-.9 1.6C6.2 10.4 1.8 6.3 1.4 2.2Z" fill="none" stroke="#f78f20" stroke-width="1.1" stroke-linejoin="round"/></svg>
      </li>
      <li>info@pfotenweide.ch
        <svg viewBox="0 0 12 12" aria-hidden="true"><rect x="1" y="2.5" width="10" height="7" rx="0.8" fill="none" stroke="#f78f20" stroke-width="1.1"/><path d="M1.3 3 6 6.5 10.7 3" fill="none" stroke="#f78f20" stroke-width="1.1"/></svg>
      </li>
      <li>www.pfotenweide.ch
        <svg viewBox="0 0 12 12" aria-hidden="true"><g fill="none" stroke="#f78f20" stroke-width="1"><circle cx="6" cy="6" r="4.8"/><ellipse cx="6" cy="6" rx="2" ry="4.8"/><path d="M1.2 6h9.6M2 3.6h8M2 8.4h8"/></g></svg>
      </li>
    </ul>
  </section>

  <section class="card card--back" aria-label="Business card back">
    <div class="card__decoration" role="img" aria-label="Large faint silhouette of a dog and a small dog in the background"></div>
    <div class="brand-mark"></div>
    <div class="brand">
      <span class="brand__name">PFOTENWEIDE</span>
      <span class="brand__url">www.pfotenweide.ch</span>
    </div>
  </section>
</body>
</html>
```